Green Ammonia PowerPoint Slides

Hi KORU Designs. You did a PowerPoint project for us previously (As BelvaGas LLC) which we very much liked and are looking for something similar in terms of design.

VerdoMolix LLC is a project development company that develops green ammonia projects. Our concept converts renewable energy from wind, solar, hydro and geothermal power sources into ammonia which can be transported by land or sea to be used as a carbon free fuel source.

We need a professional looking design for the attached PowerPoint file. The attached PowerPoint file includes the written content for each of the slides. Designers’ final product should include all the written content and be a final product for presenting to our clients with little to no more editing required.

Designer should use the graphics attached and colors as inspiration for the design. Adjacent to the logo and where used in headings it should read: “A VerdoMolix LLC Project”. Designer is free to use/modify the logo and colors however they feel provides a more interesting design and aesthetic.

Designer should include graphics, tables and charts to better present the information where it is appropriate.

The previous design you developed for us used the ETHNOCENTRIC RG font for titles, which we liked, though you are free to use any font at your discretion as long as it is free to download.

```html
<!DOCTYPE html>
<html lang="en">
<head>
<meta charset="utf-8">
<title>VerdoMolix – Cove Ltd Introduction Deck</title>
<link href="https://fonts.googleapis.com/css2?family=Orbitron:wght@700;800&family=PT+Sans:wght@400;700&display=swap" rel="stylesheet">
<style>
  :root {
    --sheet: #000000;
    --green: #0f3d27;
    --ink: #2c3a33;
    --paper: #ffffff;
    --sky-a: #8cc8bc;
    --sky-b: #d4ebe2;
    --hill-a: #a9cfc2;
    --hill-b: #5d8d7b;
    --strip: #7aa899;
    --box: #8ec5c4;
  }
  * { box-sizing: border-box; margin: 0; padding: 0; }
  html, body { width: 894px; height: 1200px; overflow: hidden; background: var(--sheet); }
  body { position: relative; font-family: "PT Sans", Arial, sans-serif; color: var(--ink); }

  .slide { position: absolute; width: 366px; height: 258px; background: var(--paper); overflow: hidden; }
  .col-l { left: 74px; } .col-r { left: 455px; }
  .row-1 { top: 74px; } .row-2 { top: 339px; } .row-3 { top: 603px; } .row-4 { top: 868px; }

  .sky { position: absolute; left: 0; top: 0; width: 100%; height: 51px;
    background: linear-gradient(100deg, var(--sky-a), var(--sky-b) 45%, var(--sky-a) 80%, #a8d6cb); }
  .hills { position: absolute; left: 0; bottom: 0; width: 100%;
    background: linear-gradient(180deg, var(--hill-a), #8fb8a8 55%, var(--hill-b)); }
  .strip { position: absolute; left: 0; bottom: 0; width: 100%; height: 15px; background: var(--strip);
    display: flex; justify-content: space-between; align-items: center; padding: 0 15px; font-size: 4.2px; color: #1f3a2e; }
  .strip b { font-weight: 700; }

  .title { position: absolute; left: 35px; font-family: "Orbitron", sans-serif; font-weight: 800;
    color: var(--green); font-size: 13.5px; line-height: 16px; letter-spacing: 0.2px; }

  .points { position: absolute; left: 38px; width: 300px; list-style: none; font-size: 5.6px; line-height: 8px; }
  .points > li { position: relative; padding-left: 9px; margin-bottom: 6px; }
  .points > li::before { content: ""; position: absolute; left: 0; top: 2px; width: 4px; height: 4px; border-radius: 50%; background: var(--green); }
  .points .src { display: block; font-size: 3.4px; line-height: 5px; font-weight: 700; color: #22302a; }
  .sub { list-style: none; margin-top: 3px; padding-left: 29px; }
  .sub li { position: relative; padding-left: 8px; margin-bottom: 2.6px; }
  .sub li::before { content: ""; position: absolute; left: 0; top: 2.4px; width: 3px; height: 3px; border-radius: 50%; background: var(--green); }
  .lead { font-weight: 700; }

  /* cover */
  .cover .sky { height: 62px; }
  .cover .band { position: absolute; top: 62px; left: 0; width: 100%; height: 80px; background: var(--paper); }
  .cover .hills { height: 116px; }
  .cover-top { position: absolute; left: 46px; top: 69px; font-family: "Orbitron", sans-serif; font-weight: 800;
    font-size: 23px; letter-spacing: 9.3px; color: var(--green); }
  .cover-big { position: absolute; left: 45px; top: 95px; font-family: "Orbitron", sans-serif; font-weight: 800;
    font-size: 42px; line-height: 42px; color: var(--green); letter-spacing: 1px; }
  .cover-tag { position: absolute; left: 202px; top: 108px; width: 118px; height: 24px; background: var(--green);
    color: #fff; font-size: 6.6px; line-height: 9.5px; padding: 2.5px 7px; }

  .flow-area { position: absolute; left: 20px; top: 90px; width: 326px; height: 118px;
    background: linear-gradient(180deg, #eef6f4, #cfe6e3 55%, #eef6f4); }
</style>
</head>
<body>

<!-- Cover -->
<section class="slide cover col-l row-1">
  <div class="sky" role="img" aria-label="Hazy teal sky with a wind turbine blade"></div>
  <div class="band"></div>
  <div class="hills" role="img" aria-label="Misty hills lined with wind turbines"></div>
  <div class="cover-top">COVERSHEET</div>
  <div class="cover-big">HERE</div>
  <div class="cover-tag">Cove Ltd - VerdoMolix Introduction<br>Date: XX/XX/XXXX</div>
</section>

<!-- Market -->
<section class="slide col-r row-1">
  <div class="sky" role="img" aria-label="Hazy teal sky with a wind turbine blade"></div>
  <h2 class="title" style="top:56px">Is There a Market?</h2>
  <ul class="points" style="top:80px;left:35px;width:300px">
    <li>The key driver is the Paris Climate Agreement which requires global commitments to carbon neutrality by 2050.</li>
    <li>Japan is one of 129 countries that have committed to achieve the Paris Climate Agreement. They need to do so without base load nuclear which remains impacted by Fukashima. Marlowe &amp; Co and others have assessed that green ammonia will have to become a major component of Japan’s energy supply to achieve that commitment.<span class="src">marloweco.example/japan-neutral</span></li>
    <li>Japan’s major power supplier has announced plans for a coal transition to ammonia commencing with 20% co-firing in 2024 which will ramp up nationally over the following decade and eventually to a full transition to Ammonia in early 2040’s. Japan has stated it will require 30MM Te per annum of green ammonia, the equivalent of 30 world scale ammonia production facilities that will require 34GW of renewable electricity.<span class="src">energywire.example/japan-ammonia</span></li>
    <li>Kitsuma Heavy have announced the worlds first 40MW ammonia fired gas turbine with an availability date of 2025. Other gas turbine suppliers will match that announcement shortly. <span class="src" style="display:inline">kitsuma.example/news</span></li>
    <li>Green Ammonia requires 3 industrial scale processes, green generation, electrolysis and ammonia synthesis. There is acknowledgment that this will not facilitate direct competition with grey and blue ammonia on price. That said, the price needs to be transparent for a market to develop and with transparency comes competition to combine the 3 industrial process. We believe Texas is positioned to deliver efficiently and effectively.<span class="src">nh3review.example/cost</span></li>
  </ul>
  <div class="strip"><span>A <b>VERDOMOLIX</b> Project</span><span>5</span></div>
</section>

<!-- Introduction -->
<section class="slide col-l row-2">
  <div class="sky" role="img" aria-label="Hazy teal sky with a wind turbine blade"></div>
  <h2 class="title" style="top:58px">Introduction</h2>
  <ul class="points" style="top:85px;width:290px">
    <li>We are VerdoMolix, experienced energy project developers who have come together with the intent of developing opportunities in North America for the production and export of green energy.</li>
    <li>Our concept converts renewable energy; wind/solar/hydro/geothermal into ammonia, the carrier for hydrogen, which can then be transported internationally to meet the accelerating demand for green renewable power generation.</li>
    <li>We are currently in the concept development stage and are looking at ammonia export from Oregon, Alaska and Texas, and have concluded that the opportunities from Texas are preferable to those on the West Coast.</li>
    <li>We have leveraged our contacts within the LNG market and have established the necessary relationship with a key Japanese buyer who has confirmed interest in base load take off.</li>
    <li>Today we present our high-level concept for developing an ammonia export project in Texas with the goal of furthering conversations with regards your appetite for partnering.</li>
  </ul>
  <div class="hills" style="height:48px" role="img" aria-label="Misty hills lined with wind turbines"></div>
  <div class="strip" style="background:transparent"><span>A <b>VERDOMOLIX</b> Project</span><span>2</span></div>
</section>

<!-- Why Texas -->
<section class="slide col-r row-2">
  <div class="sky" role="img" aria-label="Hazy teal sky with a wind turbine blade"></div>
  <h2 class="title" style="top:57px">Why Texas?</h2>
  <ul class="points" style="top:85px;left:35px;width:302px">
    <li>A project developer for Green Ammonia is no different to any other industrial development, it requires the experienced people, technology, reliable and predictable regulation, land, marine access, power infrastructure, labor, a customer and finance.</li>
    <li>Project finance favors a location with political stability (established laws) and a customer who has achieved an economically attainable low cost (competitive price supported by market IRR established via long term take off agreements).</li>
    <li>Globally the key competitors for Green Ammonia are Saudi Arabia and Australia, they each have the capacity to match Texas’ expanding renewable energy market, however each lacks one of the key financial drivers.</li>
    <li>Texas will deliver all the project requirements with specific key advantages over other USA based locations, specifically:
      <ul class="sub">
        <li>Established technical expertise grounded in world scale petrochemical execution.</li>
        <li>An established regulatory system that support industrial development.</li>
        <li>Multiple competing locations offering deep water access for international shipping.</li>
        <li>Expanding renewable power network well served by existing transmission infrastructure.</li>
        <li>An established and experienced labor pool that is globally competitive with proven delivery.</li>
      </ul>
    </li>
  </ul>
  <div class="strip"><span>A <b>VERDOMOLIX</b> Project</span><span>6</span></div>
</section>

<!-- Proposition -->
<section class="slide col-l row-3">
  <div class="sky" role="img" aria-label="Hazy teal sky with a wind turbine blade"></div>
  <h2 class="title" style="top:57px">The Proposition –<br>Why Hydrogen and Green Ammonia?</h2>
  <ul class="points" style="top:94px;width:298px">
    <li>It’s unique - Hydrogen is the only fully renewable fuel by which large quantities of energy can be efficiently transported internationally.</li>
    <li>It has a proven safety record - While hydrogen has inherent safety issue, synthesis with nitrogen into ammonia enables transport via the established international network of large ocean-going bulk carriers.</li>
    <li>It’s green - When Ammonia is re-converted back into electricity via thermal power production there is no CO2 released, catalyst technologies will mean only nitrogen and water are emitted.</li>
    <li>The color difference – Grey ammonia is currently produced using hydrogen derived from natural gas, blue ammonia is grey ammonia with carbon sequestration added, neither are green or sustainable. Green Ammonia utilizes renewable electricity to produce hydrogen via electrolysis, this is then combined with nitrogen produced from air via liquefaction. The only emission is oxygen, also a valuable bi-product.</li>
    <li>Its power friendly – Ammonia synthesis requires low power as the exothermic reaction generates steam which in turn generates power to run the ammonia facility.</li>
    <li>Technology readiness – Industrial scale modular electrolizers are market ready.</li>
  </ul>
  <div class="strip"><span>A <b>VERDOMOLIX</b> Project</span><span>3</span></div>
</section>

<!-- Partnership -->
<section class="slide col-r row-3">
  <div class="sky" style="height:47px" role="img" aria-label="Hazy teal sky with a wind turbine blade"></div>
  <h2 class="title" style="top:53px">Why a Cove Ltd and VerdoMolix<br>LLC Partnership?</h2>
  <ul class="points" style="top:90px;left:35px;width:302px">
    <li><span class="lead">Cove Ltd will provide access to:</span>
      <ul class="sub" style="padding-left:33px">
        <li>Land with marine access</li>
        <li>Low level concept funding</li>
        <li>EPC - Construction Execution with skin in the game.</li>
        <li>Initial balance sheet strength that opens the door to power purchase agreements that will backstop customer agreements.</li>
      </ul>
    </li>
    <li><span class="lead">VerdoMolix will provide access to:</span>
      <ul class="sub" style="padding-left:33px">
        <li>Lean low-cost concept delivery</li>
        <li>World scale project development expertise</li>
        <li>Technology</li>
        <li>Customer access</li>
        <li>Project finance for pre-FID and EPC</li>
      </ul>
    </li>
    <li>Together we can deliver the concept that allows the commercial offering to be finalized and presented. The site backstops the size and expansion potential, fixing the cost for power availability, EPC execution, operations and customer transport.</li>
  </ul>
  <div class="strip"><span>A <b>VERDOMOLIX</b> Project</span><span>7</span></div>
</section>

<!-- Block flow diagram -->
<section class="slide col-l row-4">
  <div class="sky" role="img" aria-label="Hazy teal sky with a wind turbine blade"></div>
  <h2 class="title" style="top:57px">Project Block Flow Diagram</h2>
  <div class="flow-area" role="img" aria-label="Project block flow diagram: renewable power and feed water through electrolysis, air separation and synthesis units to ammonia storage and a transport vessel"></div>
  <div class="hills" style="height:42px" role="img" aria-label="Misty hills lined with wind turbines"></div>
  <div class="strip" style="background:transparent"><span>A <b>VERDOMOLIX</b> Project</span><span>4</span></div>
</section>

<!-- Questions -->
<section class="slide col-r row-4">
  <div class="sky" style="height:95px" role="img" aria-label="Hazy teal sky with a wind turbine tower"></div>
  <h2 class="title" style="top:100px">Questions and Next Steps?</h2>
  <ul class="points" style="top:127px;left:35px">
    <li class="lead" style="margin-bottom:7px">Confidentiality agreement</li>
    <li class="lead" style="margin-bottom:7px">Land availability and suitability</li>
    <li class="lead">Project SPV – Agree MOU for concept select leading to customer commitment.</li>
  </ul>
  <div class="hills" style="height:73px" role="img" aria-label="Misty hills lined with wind turbines"></div>
  <div class="strip" style="background:transparent"><span>A <b>VERDOMOLIX</b> Project</span><span>8</span></div>
</section>

</body>
</html>
```